Stationery Design Project for Velmora, Chicago

Velmora, a street parking application which helps car drivers find a street parking spot by offering an ideal path along which to look for parking. This path is calculated by our algorithm based on data (e.g. historical data, baseball games schedule, etc.). Along this path the driver will find a spot and will also save 70% of the search time. Customer we target is reg. between 21 and 45 yo.

We envision something young, fresh, bright and original. Slightly abstract maybe. It should represent the idea and elements of finding street parking in the city, e.g. car(s), parking spot, people, city, etc. (just ideas!).

Logo is attached.

Requirement:
- Business Cards (2 Sided Full Color CMYK)
- Letterhead (1 Sided Full Color CMYK)
- Envelope (1 Sided Full Color CMYK)
- Sticker (1 Sided Full Color CMYK), round with a 2inch diameter.
Updates

Reason: We're starting to get more and more designs and need more time to look into all of them. Very exciting!! Thanks to everybody!

Hi all, we're in the process of selecting our favs. Though choices!!! Really good submissions. Will keep you posted and sorry for the delay.

Target Market(s)

Car drivers and owners between 21 and 45

Industry/Entity Type

Parking

Requirements
Must have
• Sticker should be round and include company URL velmora.com and the new logo which we will attach soon.
Should not have
• Should not be too serious or boring.

```html
<!DOCTYPE html>
<html lang="en">
<head>
<meta charset="utf-8">
<title>Velmora Stationery</title>
<link rel="stylesheet" href="https://fonts.googleapis.com/css2?family=Arimo:wght@400;700&display=swap">
<style>
:root{
  --board:#1d1d1d;
  --strip:#f1eff0;
  --paper:#ffffff;
  --ink:#1e1e1e;
  --navy:#1c3f78;
  --blue:#1f78c6;
  --sky:#2aa0de;
  --faint:#dce9f5;
  --label:#ffffff;
}
*{margin:0;padding:0;box-sizing:border-box}
html,body{width:1200px;height:737px;overflow:hidden;background:var(--board)}
body{position:relative;font-family:"Arimo",Arial,sans-serif}
.floor-strip{position:absolute;left:0;top:671px;width:1200px;height:66px;background:var(--strip)}
.label{position:absolute;color:var(--label);font-size:12px;white-space:nowrap}

.brand{display:flex;align-items:center;gap:7px;font-weight:700;color:var(--ink);letter-spacing:-.5px}
.brand-dot{border-radius:50%;background:var(--blue);flex:none}

/* sticker */
.sticker{position:absolute;left:92px;top:30px;width:142px;height:142px;border-radius:50%;overflow:hidden;background:var(--paper);border:3px solid var(--paper);box-shadow:0 0 0 1px #888}
.sticker-top{position:absolute;left:0;top:0;width:100%;height:42px;background:var(--blue)}
.sticker-bottom{position:absolute;left:0;top:85px;width:100%;height:60px;background:var(--ink)}
.sticker .brand{position:absolute;left:14px;top:48px;font-size:24px}
.sticker .brand-dot{width:28px;height:28px}
.sticker-url{position:absolute;top:94px;width:100%;text-align:center;color:#fff;font-size:8.5px;font-weight:700}

/* letterhead */
.letterhead{position:absolute;left:458px;top:54px;width:522px;height:645px;background:var(--paper);overflow:hidden;box-shadow:0 8px 20px rgba(0,0,0,.5)}
.letterhead .brand{position:absolute;left:65px;top:40px;font-size:29px}
.letterhead .brand-dot{width:40px;height:40px}
.letterhead-deco{position:absolute;left:389px;top:518px;width:136px;height:136px;border-radius:50%;background:var(--faint)}
.letterhead-contact{position:absolute;left:44px;top:544px}
.letterhead-url{position:absolute;left:44px;top:630px;font-size:11px;letter-spacing:1px;color:var(--ink)}

.address{color:var(--navy);font-size:9px;line-height:11px}
.contact-list{list-style:none;margin-top:13px;color:var(--navy);font-size:9px;line-height:11px}
.contact-list li{display:flex;align-items:center;gap:5px}
.contact-list li::before{content:"";width:6px;height:6px;border-radius:50%;border:1.5px solid var(--navy)}

/* envelope */
.envelope{position:absolute;left:40px;top:148px;width:677px;height:416px;filter:drop-shadow(0 6px 14px rgba(0,0,0,.45))}
.envelope svg{position:absolute;left:0;top:0}
.envelope .brand{position:absolute;left:24px;top:148px;font-size:27px}
.envelope .brand-dot{width:40px;height:40px}
.envelope .address{position:absolute;left:199px;top:164px}
.envelope-url{position:absolute;left:43px;top:400px;font-size:11px;letter-spacing:1px;color:var(--ink)}

/* business cards */
.bizcard{position:absolute;left:780px;width:366px;height:210px;box-shadow:0 8px 20px rgba(0,0,0,.5)}
.bizcard-front{top:169px;background:var(--paper)}
.bizcard-back{top:400px;background:var(--ink)}
.bizcard-front .brand{position:absolute;left:25px;top:143px;font-size:25px}
.bizcard-front .brand-dot{width:38px;height:38px}
.bizcard-info{position:absolute;left:214px;top:48px}
.bizcard-name{color:var(--navy);font-size:9px;font-weight:700;line-height:11px}
.bizcard-role{color:var(--navy);font-size:9px;line-height:11px;margin-bottom:24px}
.bizcard-url{position:absolute;left:214px;top:188px;font-size:9px;letter-spacing:1px;color:var(--ink)}
.bizcard-back-url{position:absolute;width:100%;top:112px;text-align:center;color:#fff;font-size:10.5px;letter-spacing:1px}
</style>
</head>
<body>
<div class="floor-strip"></div>

<div class="sticker">
  <div class="sticker-top"></div>
  <div class="sticker-bottom"></div>
  <div class="brand"><span class="brand-dot"></span>velmora</div>
  <div class="sticker-url">www.velmora.com</div>
</div>
<div class="label" style="left:264px;top:93px">Sticker</div>

<div class="label" style="left:491px;top:26px">Letterhead :&nbsp; US letter</div>
<section class="letterhead">
  <div class="brand"><span class="brand-dot"></span>velmora</div>
  <div class="letterhead-deco" role="img" aria-label="Faint brand mark decoration"></div>
  <div class="letterhead-contact">
    <p class="address">123 Your Drive<br>YourCity, NA 75094</p>
    <ul class="contact-list">
      <li>(312) 555-0142</li>
      <li>(312) 555-0187</li>
      <li>(312) 555-0163</li>
      <li>name@velmora.com</li>
    </ul>
  </div>
  <div class="letterhead-url">www.velmora.com</div>
</section>

<section class="envelope">
  <svg width="677" height="416" viewBox="0 0 677 416">
    <path d="M1,120 L22,84 Q27,76 38,74 L418,4 Q428,2 440,5 L655,74 Q666,78 670,90 L676,120 Z" fill="#ffffff" stroke="#cfcfcf"/>
    <text x="369" y="54" transform="rotate(180 369 54)" text-anchor="middle" font-family="Arimo, Arial, sans-serif" font-size="11" letter-spacing="1" fill="#2aa0de">www.velmora.com</text>
    <rect x="1" y="120" width="675" height="295" fill="#ffffff" stroke="#cfcfcf"/>
    <circle cx="605" cy="334" r="68" fill="#dce9f5" role="img" aria-label="Faint brand mark decoration"/>
    <rect x="41" y="236" width="279" height="100" rx="9" fill="#f2f2f2" stroke="#c9c9c9"/>
  </svg>
  <div class="brand"><span class="brand-dot"></span>velmora</div>
  <p class="address">123 Your Drive<br>YourCity, NA 75094</p>
  <div class="envelope-url">www.velmora.com</div>
</section>
<div class="label" style="left:248px;top:578px">Envelope: #10 size</div>

<div class="label" style="left:1030px;top:143px">Bizcard Front</div>
<section class="bizcard bizcard-front">
  <div class="bizcard-info">
    <p class="bizcard-name">Your name</p>
    <p class="bizcard-role">Principal</p>
    <p class="address">123 Your Drive<br>YourCity, NA 75094</p>
    <ul class="contact-list">
      <li>(312) 555-0142</li>
      <li>(312) 555-0187</li>
      <li>(312) 555-0163</li>
      <li>name@velmora.com</li>
    </ul>
  </div>
  <div class="brand"><span class="brand-dot"></span>velmora</div>
  <div class="bizcard-url">www.velmora.com</div>
</section>

<section class="bizcard bizcard-back">
  <div class="bizcard-back-url">www.velmora.com</div>
</section>
<div class="label" style="left:1030px;top:621px">Bizcard Back</div>
</body>
</html>
```